Postcard Design Project

Compliance Tools for your Ambulatory Surgery Center
from the leader in ASC Regulatory Education - Peter R. Malvanney, MBA, CASC, CPA and Harlow Crest Partners, Inc.

Three Tools Available:

1) The Clinic Rulebook Hour with Peter Malvaney
A weekly podcast for Freestanding Ambulatory Surgery Centers with Industry Leader Peter R. Malvaney, MBA, CASC, CPA. Mr. Malvaney is the author of 10 books about the ASC industry and a frequent speaker at industry meetings.
Available on Tunevault, Strevio Shelf, ViewNest, AirDial and Castleaf or visit the website at www.clinicrulebookhour.com

Books

2) Outpatient Clinic Stewardship - A Handbook for Outpatient Clinic Investors & Oversight Panel Directors
This book provides guidance to owners and board members on their responsibilities.

and

3) The Inspection Manual for Clinics - A Walkthrough of the NBRA Standards of Eligibility & Explanatory Rules for Outpatient Clinics
The industry's leading guide to preparing for a Healvera Survey.

I have provided an example of a previous post card advertising only one product - one of the books.

I am hoping to advertise the various products offered by my company (Harlow Crest Partners) and myself (Peter Malvaney) to assist Ambulatory Surgery Centers in keeping up with the latest regulations and requirements to stay in business.

Please make sure that the post card meets all of the requirements of bulk mail with the post office.

```html
<!DOCTYPE html>
<html lang="en">
<head>
<meta charset="utf-8">
<title>Clinic Compliance Tools Postcard</title>
<link rel="stylesheet" href="https://fonts.googleapis.com/css2?family=Cinzel:wght@400;600;700&family=Source+Sans+3:wght@400;600&family=Roboto+Condensed:wght@500&display=swap">
<style>
:root{
  --page:#e8e9eb;
  --navy:#17386a;
  --navy-deep:#123058;
  --band:#1f58a4;
  --sky:#8fc3f0;
  --photo-light:#e2e2e4;
  --photo-mid:#c9cacd;
  --panel:#e3e3e5;
  --white:#ffffff;
  --ink:#1e1e1e;
  --title-blue:#1e4f9c;
}
*{box-sizing:border-box;margin:0;padding:0}
html,body{width:1200px;height:1000px;overflow:hidden;background:var(--page)}
.postcard{position:absolute;top:305px;width:560px;height:390px;box-shadow:0 6px 14px rgba(0,0,0,.35);overflow:hidden}
.front{left:30px;background:var(--band)}
.back{left:610px;background:var(--white)}

/* front */
.front-header{position:absolute;left:0;top:0;width:100%;height:84px;background:var(--navy);text-align:center;padding-top:13px;font-family:"Cinzel",serif;color:var(--white)}
.front-header .headline{font-size:15.5px;line-height:18px;font-weight:400;letter-spacing:.3px}
.front-header .authors{font-size:13px;line-height:17px;font-weight:700;color:var(--sky);letter-spacing:.2px}
.photo-strip{position:absolute;left:0;top:84px;width:100%;height:196px;background:linear-gradient(90deg,var(--photo-mid),var(--photo-light) 45%,var(--photo-mid))}
.book{position:absolute;box-shadow:3px 4px 8px rgba(0,0,0,.45)}
.book-stewardship{left:66px;top:92px;width:142px;height:196px;background:linear-gradient(180deg,#1c3f78 0 42%,#5d7fa8 42% 90%,#1c3f78 90%)}
.book-inspection{left:390px;top:74px;width:124px;height:220px;background:linear-gradient(180deg,#233f93 0 28%,#6b6e74 28% 88%,#233f93 88%)}
.product{position:absolute;top:300px;text-align:center;font-family:"Cinzel",serif;color:var(--white)}
.product-left{left:4px;width:266px}
.product-right{left:280px;width:276px}
.product .title{font-size:14px;line-height:14px;font-weight:400}
.product .subtitle{font-size:7px;line-height:9px;margin-top:3px}
.product .note{font-size:7px;line-height:9px;margin-top:5px}

/* back */
.back-panel{position:absolute;left:0;top:180px;width:278px;height:210px;background:var(--panel)}
.stamp-box{position:absolute;left:456px;top:26px;width:72px;height:72px;border:1.5px solid var(--ink)}
.show-mark{position:absolute;left:160px;top:36px;width:34px;height:34px;border-radius:50%;background:var(--navy)}
.show-name{position:absolute;left:0;top:86px;width:356px;text-align:center;font-family:"Source Sans 3",sans-serif;font-size:17px;line-height:21px;font-weight:600;color:var(--ink)}
.show-name .host{display:block;color:var(--title-blue)}
.show-blurb{position:absolute;left:28px;top:142px;width:226px;height:82px;border-radius:8px;background:var(--navy-deep);box-shadow:0 3px 6px rgba(0,0,0,.35);padding:8px 6px;text-align:center;font-family:"Cinzel",serif;font-size:8.4px;line-height:10.6px;color:var(--white)}
.show-blurb .host-name{color:var(--sky);font-weight:700}
.listen-label{position:absolute;left:0;top:244px;width:278px;text-align:center;font-family:"Cinzel",serif;font-size:10px;font-weight:700;color:var(--navy)}
.platforms{position:absolute;left:14px;top:262px;width:250px;display:flex;flex-wrap:wrap;justify-content:center;gap:4px 12px;list-style:none;font-family:"Source Sans 3",sans-serif;font-size:10.5px;font-weight:600;color:var(--ink)}
.web-label{position:absolute;left:0;top:320px;width:278px;text-align:center;font-family:"Cinzel",serif;font-size:8.5px;font-weight:700;color:var(--ink)}
.web-address{position:absolute;left:0;top:334px;width:278px;text-align:center;font-family:"Roboto Condensed",sans-serif;font-size:17px;font-weight:500;color:var(--ink)}
</style>
</head>
<body>

<section class="postcard front" aria-label="Postcard front">
  <header class="front-header">
    <p class="headline">Compliance Tools for Your Ambulatory Surgery Center<br>From the Leader in ASC Regulatory Education</p>
    <p class="authors">Peter R. Malvanney, MBA, CASC, CPA and Harlow Crest Partners, Inc.</p>
  </header>
  <div class="photo-strip" role="img" aria-label="Faded photo of a surgeon in an operating room"></div>
  <div class="book book-stewardship" role="img" aria-label="Cover of the book Outpatient Clinic Stewardship"></div>
  <div class="book book-inspection" role="img" aria-label="Cover of the book The Inspection Manual for Clinics"></div>

  <div class="product product-left">
    <h2 class="title">Outpatient Clinic<br>Stewardship</h2>
    <p class="subtitle">A Handbook for Outpatient Clinic Investors<br>&amp; Oversight Panel Directors</p>
    <p class="note">This book provides guidance to owners and<br>board members on their responsibilities.</p>
  </div>
  <div class="product product-right">
    <h2 class="title">The Inspection Manual<br>for Clinics</h2>
    <p class="subtitle">A Walkthrough of the NBRA Standards of Eligibility<br>&amp; Explanatory Rules for Outpatient Clinics</p>
    <p class="note">The industry's leading guide to preparing<br>for a Healvera survey.</p>
  </div>
</section>

<section class="postcard back" aria-label="Postcard back">
  <div class="back-panel"></div>
  <div class="stamp-box"></div>
  <div class="show-mark"></div>
  <h1 class="show-name">Clinic Rulebook Hour<span class="host">with Peter Malvaney</span></h1>
  <p class="show-blurb">A weekly podcast for freestanding ambulatory surgery centers with industry leader <span class="host-name">Peter R. Malvaney, MBA, CASC, CPA.</span> Mr. Malvaney is the author of 10 books about the ASC industry and a frequent speaker at industry</p>
  <p class="listen-label">Available On</p>
  <ul class="platforms">
    <li>Tunevault</li><li>Strevio Shelf</li><li>ViewNest</li><li>AirDial</li><li>Castleaf</li>
  </ul>
  <p class="web-label">Or Visit the Website At</p>
  <p class="web-address">www.clinicrulebookhour.com</p>
</section>

</body>
</html>
```